Illustration of business process for corporate demonstration

Primary - Illustrate the below the line process with "iconology" for each step e.g:
Icon for visio
Icno for develop brief
Icon for market research
And so on for each step for a total of 21

The top line logo for Innovate and Implement large icons to be refined but intent to remain the same. The final icon/Venture Blue Harbor logo is NOT to be changed.

Venture Blue Harbor is a consultancy that specialises in assisting businesses to realise their innovation aspirations via a proven Growth Ladder – for more information please see the draft web page at https://tobin-varlow.pageloom-sites.com/

I require a visual representation of the attached process that is easy to understand and also visually stunning. You will notice that the icons above Innovate, Implement Thrive build to form the Venture Blue Harbor logo. This concept of building to form individual elements to complete an outcome is core to the Venture Blue Harbor method and needs to clearly visible for a submission to be successful.

Target Market(s)

Company owners, directors and senior executives that are looking to more innovate in their business but are time and/or resources poor.

Industry/Entity Type

Building

Requirements
Must have
• The Venture Blue Harbor final logo must not be changed in any way.

The images above Innovate and Thrive should be stylised to suit as they are only mock-ups to illustrate the concept.

Must be 1 page to suit online publication and in print materials
Should not have
• Do not change/amend the logo!

```html
<!DOCTYPE html>
<html lang="en">
<head>
<meta charset="utf-8">
<title>Growth Ladder</title>
<link rel="stylesheet" href="https://fonts.googleapis.com/css2?family=Source+Sans+3:wght@400;500&display=swap">
<style>
  :root {
    --title-green: #138a45;
    --ink: #1c1c1c;
    --icon-green: #2f8f3a;
    --icon-orange: #e9920f;
    --logo-grey: #5a5a5a;
    --logo-green: #4f9a2c;
    --bg-light: #fdfcf4;
    --bg-mid: #efeacc;
    --bg-deep: #d8d1a0;
    --arrow-start: rgba(246, 170, 40, 0.15);
    --arrow-end: #f39a12;
  }
  * { margin: 0; padding: 0; box-sizing: border-box; }
  html, body { width: 1199px; height: 1200px; overflow: hidden; }
  body {
    font-family: "Source Sans 3", Arial, sans-serif;
    color: var(--ink);
  }
  .poster {
    position: relative;
    width: 1199px;
    height: 1200px;
    overflow: hidden;
    background:
      radial-gradient(ellipse 70% 55% at 50% 32%, var(--bg-light) 0%, var(--bg-mid) 60%, transparent 100%),
      linear-gradient(180deg, var(--bg-mid) 0%, #ebe5c2 55%, var(--bg-deep) 100%);
  }
  .icon-defs { position: absolute; width: 0; height: 0; }
  .title {
    position: absolute;
    top: 22px; left: 0; width: 100%;
    text-align: center;
    font-weight: 400;
    font-size: 74px;
    letter-spacing: 1px;
    color: var(--title-green);
  }
  .stage-art { position: absolute; border-radius: 50%; }
  .art-innovate {
    left: 96px; top: 196px; width: 252px; height: 200px;
    border-radius: 18px;
    background: linear-gradient(160deg, #f2f2f2 0%, #c9c9c9 45%, #f2b81c 70%, #e99a10 100%);
  }
  .art-implement {
    left: 500px; top: 190px; width: 196px; height: 218px;
    background: radial-gradient(circle at 40% 35%, #8fd14a 0%, #2f9a2f 55%, #1c1c1c 90%);
  }
  .art-thrive {
    left: 858px; top: 182px; width: 228px; height: 228px;
    background: radial-gradient(circle at 45% 55%, #f5f5f0 0%, #c8c8c8 40%, #f3a322 65%, #47a23a 100%);
  }
  .flow-arrow { position: absolute; width: 114px; height: 56px; }
  .arrow-one { left: 354px; top: 306px; }
  .arrow-two { left: 726px; top: 306px; }

  .stage { position: absolute; top: 470px; }
  .stage-innovate { left: 106px; }
  .stage-implement { left: 488px; }
  .stage-thrive { left: 859px; }
  .stage-name {
    font-weight: 400;
    font-size: 60px;
    line-height: 1;
    margin-bottom: 44px;
  }
  .stage-thrive .stage-name { margin-left: 66px; }
  .stage-lead {
    font-size: 32px;
    line-height: 43.5px;
    margin-bottom: 43px;
  }
  .step-list { list-style: none; }
  .step {
    position: relative;
    font-size: 32px;
    line-height: 43.5px;
    white-space: nowrap;
  }
  .stage-thrive .stage-lead,
  .stage-thrive .step {
    font-size: 28.5px;
    letter-spacing: -0.3px;
  }
  .step-icon {
    position: absolute;
    left: -36px; top: 8px;
    width: 28px; height: 28px;
    color: var(--icon-green);
  }
  .stage-implement .step-icon { color: var(--icon-orange); }
  .stage-thrive .step-icon { left: -34px; top: 9px; width: 26px; height: 26px; }

  .brand {
    position: absolute;
    left: 944px; top: 1090px;
    display: flex; align-items: center; gap: 10px;
  }
  .brand-dot {
    width: 40px; height: 40px;
    border-radius: 50%;
    background: var(--logo-green);
  }
  .brand-name {
    font-weight: 500;
    font-size: 26px;
    line-height: 28px;
    color: var(--logo-grey);
    text-transform: uppercase;
  }
</style>
</head>
<body>
<svg class="icon-defs" aria-hidden="true">
  <defs>
    <linearGradient id="arrowFade" x1="0" x2="1" y1="0" y2="0">
      <stop offset="0" stop-color="var(--arrow-start)"/>
      <stop offset="1" stop-color="var(--arrow-end)"/>
    </linearGradient>
    <symbol id="i-target" viewBox="0 0 24 24"><g fill="none" stroke="currentColor" stroke-width="2"><circle cx="12" cy="12" r="10"/><circle cx="12" cy="12" r="5.5"/><circle cx="12" cy="12" r="1.5" fill="currentColor"/></g></symbol>
    <symbol id="i-doc" viewBox="0 0 24 24"><g fill="none" stroke="currentColor" stroke-width="2" stroke-linejoin="round"><path d="M5 2h10l4 4v16H5z"/><path d="M8 10h8M8 14h8M8 18h5"/></g></symbol>
    <symbol id="i-bars" viewBox="0 0 24 24"><g fill="none" stroke="currentColor" stroke-width="2"><path d="M3 21h18"/><rect x="5" y="12" width="3" height="9"/><rect x="10.5" y="7" width="3" height="14"/><rect x="16" y="3" width="3" height="18"/></g></symbol>
    <symbol id="i-diamond" viewBox="0 0 24 24"><g fill="none" stroke="currentColor" stroke-width="2" stroke-linejoin="round"><path d="M2 9l4-6h12l4 6-10 12z"/><path d="M2 9h20"/></g></symbol>
    <symbol id="i-coin" viewBox="0 0 24 24"><g fill="none" stroke="currentColor" stroke-width="2"><circle cx="12" cy="12" r="10"/><path d="M15 8.5c-1-1-5-1.5-5.5 1s5.5 1.5 5 4.5-4.5 2-5.5 1M12 5.5v13"/></g></symbol>
    <symbol id="i-boxes" viewBox="0 0 24 24"><g fill="none" stroke="currentColor" stroke-width="2"><rect x="2" y="13" width="9" height="8"/><rect x="13" y="13" width="9" height="8"/><rect x="7.5" y="3" width="9" height="8"/></g></symbol>
    <symbol id="i-note" viewBox="0 0 24 24"><g fill="none" stroke="currentColor" stroke-width="2"><rect x="2" y="6" width="20" height="12" rx="1"/><circle cx="12" cy="12" r="3"/></g></symbol>
    <symbol id="i-tick" viewBox="0 0 24 24"><g fill="none" stroke="currentColor" stroke-width="2" stroke-linecap="round"><circle cx="12" cy="12" r="10"/><path d="M7 12.5l3.5 3.5L17 9"/></g></symbol>
    <symbol id="i-inflow" viewBox="0 0 24 24"><g fill="none" stroke="currentColor" stroke-width="2" stroke-linecap="round"><path d="M12 2v11M7.5 8.5L12 13l4.5-4.5"/><path d="M3 14v7h18v-7"/></g></symbol>
    <symbol id="i-flow" viewBox="0 0 24 24"><g fill="none" stroke="currentColor" stroke-width="2"><rect x="2" y="3" width="8" height="6"/><rect x="14" y="15" width="8" height="6"/><path d="M6 9v9h8"/></g></symbol>
    <symbol id="i-wrench" viewBox="0 0 24 24"><g fill="none" stroke="currentColor" stroke-width="2" stroke-linecap="round" stroke-linejoin="round"><path d="M14.5 3a5 5 0 0 0-4.8 6.6L3 16.3V21h4.7l6.7-6.7A5 5 0 0 0 21 9.5l-3 3-3.5-1-1-3.5 3-3A5 5 0 0 0 14.5 3z"/></g></symbol>
    <symbol id="i-line" viewBox="0 0 24 24"><g fill="none" stroke="currentColor" stroke-width="2" stroke-linecap="round" stroke-linejoin="round"><path d="M3 3v18h18"/><path d="M6 16l4-5 4 3 6-8"/></g></symbol>
    <symbol id="i-warn" viewBox="0 0 24 24"><g fill="none" stroke="currentColor" stroke-width="2" stroke-linejoin="round" stroke-linecap="round"><path d="M12 2.5L22 20.5H2z"/><path d="M12 9v5.5M12 17.5v.5"/></g></symbol>
    <symbol id="i-chat" viewBox="0 0 24 24"><g fill="none" stroke="currentColor" stroke-width="2" stroke-linejoin="round"><path d="M3 4h18v12H10l-5 4v-4H3z"/><path d="M7 9h10M7 12h6"/></g></symbol>
    <symbol id="i-bulb" viewBox="0 0 24 24"><g fill="none" stroke="currentColor" stroke-width="2" stroke-linecap="round"><path d="M9 17v-2.5A6.5 6.5 0 1 1 15 14.5V17z"/><path d="M9.5 20.5h5"/></g></symbol>
    <symbol id="i-flag" viewBox="0 0 24 24"><g fill="none" stroke="currentColor" stroke-width="2" stroke-linejoin="round" stroke-linecap="round"><path d="M5 22V3"/><path d="M5 4h13l-3 4.5 3 4.5H5"/></g></symbol>
    <symbol id="i-rise" viewBox="0 0 24 24"><g fill="none" stroke="currentColor" stroke-width="2" stroke-linecap="round" stroke-linejoin="round"><path d="M3 18l6-6 4 4 8-9"/><path d="M15 7h6v6"/></g></symbol>
    <symbol id="i-horn" viewBox="0 0 24 24"><g fill="none" stroke="currentColor" stroke-width="2" stroke-linejoin="round"><path d="M3 9h4l10-5v16L7 15H3z"/><path d="M7 15l2 6h3l-1.5-5"/></g></symbol>
    <symbol id="i-gauge" viewBox="0 0 24 24"><g fill="none" stroke="currentColor" stroke-width="2" stroke-linecap="round"><path d="M3 18a9 9 0 1 1 18 0"/><path d="M12 18l4.5-6"/><circle cx="12" cy="18" r="1.2" fill="currentColor"/></g></symbol>
    <symbol id="i-chain" viewBox="0 0 24 24"><g fill="none" stroke="currentColor" stroke-width="2"><rect x="1.5" y="9" width="6" height="6"/><rect x="16.5" y="9" width="6" height="6"/><rect x="9" y="3" width="6" height="6"/><path d="M7.5 12h9M12 9v3"/></g></symbol>
    <symbol id="i-steps" viewBox="0 0 24 24"><g fill="none" stroke="currentColor" stroke-width="2" stroke-linejoin="round" stroke-linecap="round"><path d="M2 21h5v-5h5v-5h5V6h5"/><path d="M17 2h5v4"/></g></symbol>
  </defs>
</svg>

<main class="poster">
  <h1 class="title">GROWTH LADDER</h1>

  <div class="stage-art art-innovate" role="img" aria-label="Icon of a magnifying glass over a search bar with a green leaf"></div>
  <svg class="flow-arrow arrow-one" viewBox="0 0 114 56" aria-hidden="true">
    <polygon points="0,16 74,16 74,0 114,28 74,56 74,40 0,40" fill="url(#arrowFade)"/>
  </svg>
  <div class="stage-art art-implement" role="img" aria-label="Icon of a green globe with an orange swirl"></div>
  <svg class="flow-arrow arrow-two" viewBox="0 0 114 56" aria-hidden="true">
    <polygon points="0,16 74,16 74,0 114,28 74,56 74,40 0,40" fill="url(#arrowFade)"/>
  </svg>
  <div class="stage-art art-thrive" role="img" aria-label="Icon of a light bulb and small globe inside circular recycling arrows"></div>

  <section class="stage stage-innovate">
    <h2 class="stage-name">Innovate</h2>
    <p class="stage-lead">Refine concept:</p>
    <ol class="step-list">
      <li class="step"><svg class="step-icon" aria-hidden="true"><use href="#i-target"/></svg>1.Vision your goal</li>
      <li class="step"><svg class="step-icon" aria-hidden="true"><use href="#i-doc"/></svg>2.Develop Brief</li>
      <li class="step"><svg class="step-icon" aria-hidden="true"><use href="#i-bars"/></svg>3.Market Research</li>
      <li class="step"><svg class="step-icon" aria-hidden="true"><use href="#i-diamond"/></svg>4.Define Value</li>
      <li class="step"><svg class="step-icon" aria-hidden="true"><use href="#i-coin"/></svg>5.Budget Project</li>
      <li class="step"><svg class="step-icon" aria-hidden="true"><use href="#i-boxes"/></svg>6.Allocate Resources</li>
      <li class="step"><svg class="step-icon" aria-hidden="true"><use href="#i-note"/></svg>7.Identify Funding</li>
    </ol>
  </section>

  <section class="stage stage-implement">
    <h2 class="stage-name">Implement</h2>
    <p class="stage-lead">Drive outcomes:</p>
    <ol class="step-list">
      <li class="step"><svg class="step-icon" aria-hidden="true"><use href="#i-tick"/></svg>1.Project accountability</li>
      <li class="step"><svg class="step-icon" aria-hidden="true"><use href="#i-inflow"/></svg>2.Source funding</li>
      <li class="step"><svg class="step-icon" aria-hidden="true"><use href="#i-flow"/></svg>3.Program Development</li>
      <li class="step"><svg class="step-icon" aria-hidden="true"><use href="#i-wrench"/></svg>4.Operation Capabilities</li>
      <li class="step"><svg class="step-icon" aria-hidden="true"><use href="#i-line"/></svg>5.Financial Modelling</li>
      <li class="step"><svg class="step-icon" aria-hidden="true"><use href="#i-warn"/></svg>6.Risk Management</li>
      <li class="step"><svg class="step-icon" aria-hidden="true"><use href="#i-chat"/></svg>7.Client Engagement</li>
    </ol>
  </section>

  <section class="stage stage-thrive">
    <h2 class="stage-name">Thrive</h2>
    <p class="stage-lead">Manage Results:</p>
    <ol class="step-list">
      <li class="step"><svg class="step-icon" aria-hidden="true"><use href="#i-bulb"/></svg>1.Innovation culture</li>
      <li class="step"><svg class="step-icon" aria-hidden="true"><use href="#i-flag"/></svg>2.Management Strategy</li>
      <li class="step"><svg class="step-icon" aria-hidden="true"><use href="#i-rise"/></svg>3.Revenue Forecasting</li>
      <li class="step"><svg class="step-icon" aria-hidden="true"><use href="#i-horn"/></svg>4.Promotional Activity</li>
      <li class="step"><svg class="step-icon" aria-hidden="true"><use href="#i-gauge"/></svg>5.BusinessProcesses &amp; KPI’s</li>
      <li class="step"><svg class="step-icon" aria-hidden="true"><use href="#i-chain"/></svg>6.Supply chain engagement</li>
      <li class="step"><svg class="step-icon" aria-hidden="true"><use href="#i-steps"/></svg>7.Growth Planning</li>
    </ol>
  </section>

  <div class="brand">
    <span class="brand-dot" aria-hidden="true"></span>
    <span class="brand-name">Venture Blue<br>Harbor</span>
  </div>
</main>
</body>
</html>
```